its a new company based in Christchurch new Zealand building computers ,repairs, upgrades and anything computers for the general public,i like bright happy colours like yellows, greens reds anything that stands out and it needs to communicant trust and security towards my new company,i have no logo yet,

Target Market(s)

target market of all ages

Industry/Entity Type

Building

Contact Information for Business Card

Pixel Harbour Limited,ph-0274829315,email-brightnode47@mailvista.example,14c tamworth cl,kelvale

```html
<!DOCTYPE html>
<html lang="en">
<head>
<meta charset="utf-8">
<title>Pixel Harbour Limited – Business Card</title>
<link rel="stylesheet" href="https://fonts.googleapis.com/css2?family=Righteous&family=Open+Sans:wght@400;600&display=swap">
<style>
  :root {
    --page-bg: #2a2a2e;
    --card-light: #d4effb;
    --card-mid: #6cc3ee;
    --card-deep: #1f86cf;
    --title-top: #ffd53a;
    --title-bottom: #e89a0c;
    --title-shadow: #7a4a05;
    --contact-text: #ffffff;
    --icon-yellow: #ffe21a;
    --art-dark: #1c2430;
    --art-gold: #e0a928;
  }
  * { margin: 0; padding: 0; box-sizing: border-box; }
  html, body {
    width: 1200px;
    height: 800px;
    overflow: hidden;
    background: var(--page-bg);
  }
  .stage {
    width: 1200px;
    height: 800px;
    display: flex;
    align-items: center;
    justify-content: center;
  }
  .business-card {
    position: relative;
    width: 920px;
    height: 526px;
    overflow: hidden;
    border-radius: 4px;
    box-shadow: 0 18px 40px rgba(0,0,0,0.45);
  }
  .card-backdrop {
    position: absolute;
    inset: 0;
    background:
      radial-gradient(ellipse at 20% 55%, rgba(255,255,255,0.55), transparent 55%),
      linear-gradient(120deg, var(--card-light) 0%, var(--card-mid) 45%, var(--card-deep) 100%);
  }
  .product-artwork {
    position: absolute;
    left: 40px;
    top: 130px;
    width: 240px;
    height: 230px;
    border-radius: 10px;
    background:
      radial-gradient(ellipse at 35% 20%, var(--art-gold) 0%, rgba(224,169,40,0) 32%),
      linear-gradient(160deg, #3a4a5e 0%, var(--art-dark) 60%, #2d5da8 100%);
    opacity: 0.92;
  }
  .company-name {
    position: absolute;
    left: 300px;
    top: 70px;
    font-family: "Righteous", sans-serif;
    font-weight: 400;
    font-size: 76px;
    line-height: 1;
    color: var(--title-top);
    background: linear-gradient(180deg, var(--title-top) 30%, var(--title-bottom) 80%);
    -webkit-background-clip: text;
    background-clip: text;
    -webkit-text-fill-color: transparent;
    filter: drop-shadow(3px 4px 0 var(--title-shadow));
  }
  .company-name span { display: block; }
  .company-name .line-two { padding-left: 20px; }
  .contact-list {
    position: absolute;
    left: 300px;
    top: 320px;
    list-style: none;
    font-family: "Open Sans", sans-serif;
    font-weight: 400;
    font-size: 30px;
    line-height: 48px;
    color: var(--contact-text);
    text-shadow: 1px 2px 3px rgba(0,40,90,0.35);
  }
  .contact-item {
    display: flex;
    align-items: center;
    gap: 12px;
    white-space: nowrap;
  }
  .contact-icon {
    width: 26px;
    height: 26px;
    flex: none;
  }
  .contact-icon path { fill: var(--icon-yellow); }
</style>
</head>
<body>
<main class="stage">
  <article class="business-card">
    <div class="card-backdrop" role="img" aria-label="Bright blue technology backdrop with a fine wireframe grid"></div>
    <div class="product-artwork" role="img" aria-label="Illustration of a black computer tower wearing a gold crown beside a monitor"></div>

    <h1 class="company-name">
      <span class="line-one">Pixel Harbour</span>
      <span class="line-two">Limited</span>
    </h1>

    <ul class="contact-list">
      <li class="contact-item">
        <svg class="contact-icon" viewBox="0 0 24 24" aria-hidden="true">
          <path d="M6.6 10.8a15.2 15.2 0 0 0 6.6 6.6l2.2-2.2a1 1 0 0 1 1-.25 11.4 11.4 0 0 0 3.6.57 1 1 0 0 1 1 1V20a1 1 0 0 1-1 1A17 17 0 0 1 3 4a1 1 0 0 1 1-1h3.5a1 1 0 0 1 1 1c0 1.25.2 2.450.57 3.57a1 1 0 0 1-.25 1z"/>
        </svg>
        <span>0274829315,</span>
      </li>
      <li class="contact-item">
        <svg class="contact-icon" viewBox="0 0 24 24" aria-hidden="true">
          <path d="M2 5h20v14H2zM4 7v.4l8 5.2 8-5.2V7zM4 9.8V17h16V9.8l-8 5.2z" fill-rule="evenodd"/>
        </svg>
        <span>brightnode47@mailvista.example,</span>
      </li>
      <li class="contact-item">
        <svg class="contact-icon" viewBox="0 0 24 24" aria-hidden="true">
          <path d="M12 2 1 12h3v10h6v-6h4v6h6V12h3z"/>
        </svg>
        <span>14c tamworth cl,kelvale</span>
      </li>
    </ul>
  </article>
</main>
</body>
</html>
```